Refresh Application User Interface

Pellmark wishes to update the look of its business applications. Two representative forms are shown below. Please note, we are not considering changes in functionality or usability. Our goal is a cleaner, more contemporary design.

Industry/Entity Type

Business

```html
<!DOCTYPE html>
<html lang="en">
<head>
<meta charset="utf-8">
<title>Pellmark – Purchase Order</title>
<link href="https://fonts.googleapis.com/css2?family=Roboto:wght@400;500;700&display=swap" rel="stylesheet">
<style>
:root{
  --blue:#0a4f9f;
  --green:#a0d468;
  --green-dark:#79b043;
  --green-text:#8cc95a;
  --ink:#333;
  --red:#d9352b;
  --row-alt:#ececec;
  --line:#c9c9c9;
}
*{box-sizing:border-box;margin:0;padding:0}
html,body{width:1200px;height:1170px;overflow:hidden;background:#fff;font-family:Roboto,sans-serif;color:var(--ink)}
.abs{position:absolute}
.topbar{left:0;top:0;width:1200px;height:50px;background:var(--blue);color:#fff;font-size:18px}
.topbar span{position:absolute;top:14px}
.user-box{position:absolute;left:130px;top:0;width:134px;height:50px;background:var(--green);font-weight:500}
.role-box{position:absolute;left:383px;top:0;width:153px;height:50px;background:var(--green);font-weight:500}
.toplinks{position:absolute;right:16px;top:16px;font-size:15px;display:flex}
.toplinks a{color:#fff;text-decoration:none;padding:0 9px;border-left:1px solid #fff;line-height:18px}
.toplinks a:first-child{border-left:none}
.modules{left:10px;top:65px;display:flex;height:33px}
.modules div{background:var(--blue);color:#fff;font-size:19px;height:33px;line-height:33px;text-align:center;border-right:1px solid #fff}
.modules .on{background:var(--green);margin-top:0}
.brand{left:1032px;top:66px;font-size:26px;font-weight:700;color:var(--blue);letter-spacing:1px}
.subnav{left:0;top:98px;width:1200px;height:41px;background:var(--green);display:flex;padding-left:20px}
.subnav div{color:#fff;font-size:15px;line-height:41px;padding:0 9px}
.subnav .on{background:var(--green-dark)}
h1{position:absolute;left:133px;top:160px;font-size:36px;font-weight:700;color:#2b2b2b}
.tabs{left:667px;top:169px;display:flex}
.tabs div{width:101px;height:33px;line-height:33px;text-align:center;color:#fff;font-weight:700;font-size:17px;background:var(--blue);border-right:1px solid #fff;border-radius:4px 4px 0 0}
.tabs .on{background:var(--green)}
.panel{left:130px;top:202px;width:940px;height:883px;border:2px solid var(--green)}
.toolbar{left:130px;top:202px;width:940px;height:35px;background:var(--green)}
.tb{position:absolute;top:0;height:35px;background:var(--blue);color:#fff;display:flex;align-items:center;justify-content:center;font-size:16px;font-weight:500;border-right:1px solid #3f74b5;gap:7px}
.ordbox{left:147px;top:252px;width:906px;height:90px;border:1px solid var(--green)}
.ordno{position:absolute;left:19px;top:18px;font-size:16px;font-weight:500}
.ordtype{position:absolute;left:187px;top:18px;font-size:16px;font-weight:500;color:var(--green-text)}
.vendor{position:absolute;left:178px;top:45px;width:320px;height:20px;background:#e6e6e6;font-size:12px;line-height:20px;padding-left:10px}
.hold{position:absolute;right:20px;top:18px;font-size:16px;font-weight:500;color:var(--blue)}
.gbtn{position:absolute;top:362px;width:34px;height:34px;background:var(--green);display:flex;align-items:center;justify-content:center}
.pager{left:826px;top:366px;font-size:18px;display:flex;align-items:center;gap:8px}
.pager b{color:var(--green-text);font-weight:400}
.head{top:406px;font-size:14px}
.row{left:147px;width:906px}
.inp{position:absolute;height:26px;border:1px solid var(--line);background:#fff;font-size:16px;line-height:24px;padding-left:10px}
.sel::after{content:"";position:absolute;right:9px;top:8px;width:6px;height:6px;border-right:2px solid var(--green-text);border-bottom:2px solid var(--green-text);transform:rotate(45deg)}
.desc{font-size:12px;height:24px;line-height:22px}
.chk{position:absolute;width:18px;height:18px;border:1px solid var(--line);background:#fff;border-radius:2px}
.t{position:absolute;font-size:14px}
.num{color:var(--green-text)}
.red{color:var(--red);font-weight:500}
.lineno{position:absolute;font-size:20px;color:var(--green-text);font-weight:500}
.status{left:0;top:1110px;width:1200px;height:60px;background:var(--blue)}
.status .msg{position:absolute;left:335px;top:0;width:537px;height:60px;background:var(--green);color:#fff;font-size:18px;font-weight:500;line-height:62px;padding-left:75px}
</style>
</head>
<body>

<div class="abs topbar">
  <span style="left:17px">Logged In As</span>
  <div class="user-box"><span style="left:9px">Dana Moreau ⚙</span></div>
  <span style="left:273px">Current Role</span>
  <div class="role-box"><span style="left:8px">Administrator ▾</span></div>
  <div class="toplinks"><a>Touch</a><a>New Tab</a><a>Help</a><a>Support</a><a>Log out</a></div>
</div>

<div class="abs modules">
  <div style="width:87px">Home</div><div style="width:88px">eSource</div><div class="on" style="width:88px">eBuy</div><div style="width:97px">eRequest</div><div style="width:88px">eSell</div><div style="width:88px">eStock</div><div style="width:87px">ePlan</div><div style="width:111px">Preferences</div>
</div>
<div class="abs brand">PELLMARK</div>

<div class="abs subnav">
  <div class="on">Orders</div><div>Receipts</div><div>Shipments</div><div>Invoices</div><div>Pricing</div><div>Tables</div><div>Reports</div><div>Inquiries</div><div>Periodic Tasks</div><div>Workflows</div>
</div>

<h1>Purchase Order</h1>
<div class="abs tabs"><div>Header</div><div class="on">Lines</div><div>Charges</div><div>Notes<sup style="color:var(--green)">●</sup></div></div>

<div class="abs panel"></div>
<div class="abs toolbar">
  <div class="tb" style="left:2px;width:36px">📎</div>
  <div class="tb" style="left:38px;width:36px">▤</div>
  <div class="tb" style="left:74px;width:36px">⋖</div>
  <div class="tb" style="left:110px;width:36px">🔧</div>
  <div class="tb" style="left:146px;width:36px">?</div>
  <div class="tb" style="left:182px;width:120px">↗ Post Order</div>
  <div class="tb" style="left:484px;width:90px">⌕ search</div>
  <div class="tb" style="left:574px;width:91px"><span style="color:var(--green)">⊕</span> new</div>
  <div class="tb" style="left:665px;width:91px"><span style="color:var(--green)">✓</span> apply</div>
  <div class="tb" style="left:756px;width:91px"><span style="color:var(--red)">▮</span> delete</div>
  <div class="tb" style="left:847px;width:91px">↺ back</div>
</div>

<div class="abs ordbox">
  <div class="ordno">Order #100159</div>
  <div class="ordtype">Regular Purchase Order</div>
  <div class="vendor">Harbor Clinical Goods, Westbrook ME</div>
  <div class="hold">Hold for Completion</div>
</div>

<div class="gbtn" style="left:147px"><svg width="18" height="18"><text x="2" y="16" fill="#fff" font-size="20" font-weight="700">Σ</text></svg></div>
<div class="gbtn" style="left:183px"><svg width="18" height="20"><rect x="5" y="1" width="12" height="14" fill="#fff"/><rect x="1" y="5" width="12" height="14" fill="#fff" stroke="#a0d468"/></svg></div>
<div class="gbtn" style="left:219px"><svg width="18" height="20"><rect x="2" y="2" width="10" height="14" fill="#fff"/><rect x="6" y="6" width="11" height="13" fill="#fff" stroke="#a0d468"/></svg></div>
<div class="gbtn" style="left:255px"><svg width="20" height="20"><path d="M1 2h18l-7 8v9l-4-3v-6z" fill="#fff"/></svg></div>
<div class="gbtn" style="left:291px"><svg width="20" height="20"><circle cx="10" cy="10" r="9" fill="#fff"/><path d="M6 6l8 8M14 6l-8 8" stroke="#a0d468" stroke-width="2.5"/></svg></div>

<div class="abs pager"><span style="color:var(--green-text)">⏮ ⏪</span><span style="margin-left:10px">Page <b>1</b> of <b>1</b></span><span style="color:var(--green-text)">⏩ ⏭</span></div>

<div class="abs head" style="left:156px">Line <small>#</small></div>
<div class="abs head" style="left:255px">Product</div>
<div class="abs head" style="left:385px">Supplier #</div>
<div class="abs head" style="left:458px">Open Qty</div>
<div class="abs head" style="left:568px">Unit</div>
<div class="abs head" style="left:642px">Unit Price</div>
<div class="abs head" style="left:747px">Extended</div>
<div class="abs head" style="left:856px">LI Type / Ship to</div>
<div class="chk" style="left:1027px;top:406px"></div>

<div class="abs row" style="top:430px;height:107px">
  <div class="lineno" style="left:24px;top:14px">1</div>
  <div class="inp" style="left:58px;top:14px;width:160px">P-1200</div>
  <div class="t num" style="left:222px;top:18px;font-size:18px">⚲</div>
  <div class="chk" style="left:260px;top:18px"></div>
  <div class="inp" style="left:311px;top:14px;width:100px">1</div>
  <div class="inp sel" style="left:421px;top:14px;width:65px">Ea</div>
  <div class="inp" style="left:496px;top:14px;width:75px">$6.50</div>
  <div class="t" style="left:602px;top:17px;font-size:16px">$6.50</div>
  <div class="inp sel" style="left:709px;top:14px;width:143px">Receive&amp;Pay</div>
  <div class="chk" style="left:880px;top:18px"></div>
  <div class="inp desc" style="left:58px;top:45px;width:513px">Brightleaf 3893117 - Brochure Paper, Ultra Smooth Text, 8 1/2" x 11" lb., 96 Brightness</div>
  <div class="t num" style="left:603px;top:51px">ALCH</div>
  <div class="inp sel" style="left:709px;top:45px;width:143px"></div>
  <div class="t" style="left:106px;top:76px">On Purchase Orders <span class="num" style="margin-left:6px">30</span></div>
  <div class="t" style="left:311px;top:76px">Available <span class="num" style="margin-left:6px">0</span></div>
  <div class="t red" style="left:494px;top:77px">Over Budget</div>
  <div class="t red" style="left:603px;top:77px">Pending</div>
  <svg class="abs" style="left:730px;top:74px" width="14" height="18"><path d="M0 0h9l5 5v13H0z" fill="#a0d468"/></svg>
  <svg class="abs" style="left:785px;top:74px" width="18" height="18"><rect y="3" width="18" height="15" fill="#a0d468"/><rect x="3" width="3" height="5" fill="#a0d468"/><rect x="12" width="3" height="5" fill="#a0d468"/><path d="M0 7h18" stroke="#fff"/></svg>
</div>

<div class="abs row" style="top:538px;height:102px;background:var(--row-alt)">
  <div class="lineno" style="left:24px;top:14px">2</div>
  <div class="inp" style="left:58px;top:14px;width:160px">P-1100</div>
  <div class="t num" style="left:222px;top:18px;font-size:18px">⚲</div>
  <div class="chk" style="left:260px;top:18px"></div>
  <div class="inp" style="left:311px;top:14px;width:100px">1</div>
  <div class="inp sel" style="left:421px;top:14px;width:65px">Ea</div>
  <div class="inp" style="left:496px;top:14px;width:75px">$5.00</div>
  <div class="t" style="left:602px;top:17px;font-size:16px">$5.00</div>
  <div class="inp sel" style="left:709px;top:14px;width:143px">Receive&amp;Pay</div>
  <div class="chk" style="left:880px;top:18px"></div>
  <div class="inp desc" style="left:58px;top:45px;width:513px">Northcove 454230 - Recycled Laser Paper 1 case(2,500 count) - 24lb, 90 bright</div>
  <div class="t num" style="left:603px;top:51px">ALCH</div>
  <div class="inp sel" style="left:709px;top:45px;width:143px"></div>
  <div class="t" style="left:106px;top:76px">On Purchase Orders <span class="num" style="margin-left:6px">170</span></div>
  <div class="t" style="left:311px;top:76px">Available <span class="num" style="margin-left:6px">0</span></div>
  <div class="t red" style="left:494px;top:77px">Over Budget</div>
  <div class="t red" style="left:603px;top:77px">Pending</div>
  <svg class="abs" style="left:730px;top:74px" width="14" height="18"><path d="M0 0h9l5 5v13H0z" fill="#a0d468"/></svg>
  <svg class="abs" style="left:785px;top:74px" width="18" height="18"><rect y="3" width="18" height="15" fill="#a0d468"/><rect x="3" width="3" height="5" fill="#a0d468"/><rect x="12" width="3" height="5" fill="#a0d468"/><path d="M0 7h18" stroke="#fff"/></svg>
</div>

<div class="abs row" style="top:645px;height:75px">
  <div class="inp" style="left:9px;top:12px;width:41px"></div>
  <div class="inp" style="left:58px;top:12px;width:160px"></div>
  <div class="t num" style="left:222px;top:16px;font-size:18px">⚲</div>
  <div class="chk" style="left:260px;top:16px"></div>
  <div class="inp" style="left:311px;top:12px;width:100px"></div>
  <div class="inp sel" style="left:421px;top:12px;width:65px"></div>
  <div class="inp" style="left:496px;top:12px;width:75px"></div>
  <div class="inp sel" style="left:709px;top:12px;width:143px">Receive&amp;Pay</div>
  <div class="chk" style="left:880px;top:16px"></div>
  <div class="inp desc" style="left:58px;top:43px;width:513px"></div>
  <div class="inp sel" style="left:709px;top:43px;width:143px"></div>
</div>

<div class="abs status">
  <div class="msg">
    <svg class="abs" style="left:20px;top:16px" width="32" height="30"><path d="M2 2h28v20H14l-8 7v-7H2z" fill="#fff"/></svg>
    Click Search, or enter property values and click Apply
  </div>
</div>

</body>
</html>
```